Diverse, up-scale salon needs eye-catching, unique business cards.

We are looking for a unique business card design for our stylist but that can also be multi functional and used for appointment reminder and referrals. I will need a design in a format that I can modify names and titles going forward. In the past we have had a dark background with the logo on one side, and stylist and contact information on the other but we are open to all ideas. I have included our mission statement as well as branded colors below. The statement doesn't need to go on the card, it's just a reference for target market. We need space for the stylists name, title, instagram handle and then the salons phone number, website and address. I am also open to adding a spot for a qr code linked to the stylist instagram or the salon booking link.

primary brand colors:
#333333 #233415 #36502a #93874a #000000
Mission statement:
Morvane Hair Studio, a high-end salon located in the lively Downtown Farmington, Michigan, is committed to providing exceptional services in a welcoming and relaxed environment to meet the needs of our diverse clientele.
Our salon specializes in contemporary custom haircuts, coloring, extensions, and barbering and beard grooming services. Our team of skilled stylists is passionate and inventive in their hair styling techniques. At the heart of our salon are values centered on quality, innovation, creativity, and above all, comfort. These core values are evident in every appointment across our customizable array of services.
Our goal is to establish a benchmark for exceptional hair care for every human.
Website: www.morvanehairstudio-demo.com
instagram: @morvanehairstudio
address: 41872 Pelton Brook Rd, Farmington MI
phone: 248-316-8847

Industry/Entity Type

Hair Salon

Contact Information for Business Card

Stylist name, title, phone, instagram, website, address, (optional qr code)

Requirements
Should not have
• Does not need mission statement on the card.

```html
<!DOCTYPE html>
<html lang="en">
<head>
<meta charset="utf-8">
<title>Morvane Hair Studio – Business Card</title>
<link href="https://fonts.googleapis.com/css2?family=Poppins:wght@300;400;500&display=swap" rel="stylesheet">
<style>
  :root {
    --backdrop: #9c9576;
    --card: #121212;
    --gold: #94874a;
    --text-light: #e9e6dc;
    --faint: #1c1c1c;
    --rule: #6f6746;
  }
  * { box-sizing: border-box; margin: 0; padding: 0; }
  html, body {
    width: 676px; height: 1200px; overflow: hidden;
    background: var(--backdrop);
    font-family: "Poppins", sans-serif;
  }
  .card {
    position: absolute; left: 38px;
    width: 600px; height: 343px;
    background: var(--card);
    overflow: hidden;
  }
  .card--front { top: 227px; }
  .card--back { top: 630px; }

  .faint-name {
    position: absolute; right: -20px;
    font-weight: 500; font-size: 64px; letter-spacing: 4px;
    color: var(--faint); line-height: 1; white-space: nowrap;
  }
  .card--front .faint-name { top: 150px; }
  .card--back .faint-name { top: 40px; }

  .brand {
    position: absolute;
    display: flex; flex-direction: column; align-items: center; gap: 12px;
    transform: translate(-50%, -50%);
  }
  .brand__dot {
    width: 18px; height: 18px; border-radius: 50%;
    background: var(--gold);
  }
  .brand__name {
    color: var(--gold); font-weight: 500;
    font-size: 24px; letter-spacing: 3px; text-transform: uppercase;
    text-align: center; line-height: 1.25;
  }
  .card--front .brand { left: 300px; top: 148px; }
  .card--back .brand { left: 144px; top: 175px; }
  .card--back .brand__name { font-size: 21px; }

  .services {
    position: absolute; left: 40px; top: 265px;
    width: 525px; height: 41px;
    border: 1px solid var(--rule); border-radius: 6px;
    display: flex; align-items: center;
  }
  .services__item {
    height: 100%;
    display: flex; align-items: center; justify-content: center;
    color: var(--text-light); font-size: 9.5px; line-height: 1.35;
    text-transform: uppercase; text-align: left;
  }
  .services__item + .services__item { border-left: 1px solid var(--text-light); height: 30px; }
  .services__item:nth-child(1) { width: 113px; padding-left: 4px; }
  .services__item:nth-child(2) { width: 96px; }
  .services__item:nth-child(3) { width: 104px; }
  .services__item:nth-child(4) { width: 94px; }
  .services__item:nth-child(5) { width: 118px; }

  .contact { position: absolute; left: 314px; top: 80px; }
  .contact__name {
    color: var(--gold); font-weight: 300;
    font-size: 19px; letter-spacing: 2.5px; text-transform: uppercase;
    line-height: 1.2;
  }
  .contact__title {
    color: var(--text-light); font-weight: 500;
    font-size: 11.5px; letter-spacing: 2.5px; text-transform: uppercase;
    margin-top: 2px;
  }
  .contact__list { list-style: none; margin-top: 20px; }
  .contact__row {
    display: flex; align-items: flex-start; gap: 14px;
    color: var(--text-light); font-weight: 300;
    font-size: 13.5px; line-height: 1.3; margin-bottom: 11px;
  }
  .contact__icon { width: 17px; height: 17px; flex: none; margin-top: 1px; }
  .contact__icon * { fill: none; stroke: var(--gold); stroke-width: 1.4; stroke-linecap: round; stroke-linejoin: round; }
</style>
</head>
<body>

<section class="card card--front">
  <div class="faint-name" aria-hidden="true">MORVANE</div>
  <div class="brand">
    <span class="brand__dot"></span>
    <span class="brand__name">Morvane<br>Hair Studio</span>
  </div>
  <ul class="services">
    <li class="services__item">Contemporary<br>Custom Haircuts</li>
    <li class="services__item">Coloring</li>
    <li class="services__item">Extensions</li>
    <li class="services__item">Barbering</li>
    <li class="services__item">Beard Grooming</li>
  </ul>
</section>

<section class="card card--back">
  <div class="faint-name" aria-hidden="true">MORVANE</div>
  <div class="brand">
    <span class="brand__dot"></span>
    <span class="brand__name">Morvane<br>Hair Studio</span>
  </div>
  <div class="contact">
    <h1 class="contact__name">Dana Whitfield</h1>
    <p class="contact__title">CEO, Founder</p>
    <ul class="contact__list">
      <li class="contact__row">
        <svg class="contact__icon" viewBox="0 0 24 24"><path d="M5 3h4l2 5-2.5 1.5a11 11 0 0 0 6 6L16 13l5 2v4a2 2 0 0 1-2 2A17 17 0 0 1 3 5a2 2 0 0 1 2-2z"/><path d="M15 3a6 6 0 0 1 6 6M15 7a2 2 0 0 1 2 2"/></svg>
        <span>248-316-8847</span>
      </li>
      <li class="contact__row">
        <svg class="contact__icon" viewBox="0 0 24 24"><path d="M12 21s-6-6-6-11a6 6 0 0 1 12 0c0 5-6 11-6 11z"/><circle cx="12" cy="10" r="2.2"/><path d="M7 19c-2 .5-3 1-3 1.5S7 22 12 22s8-.8 8-1.5-1-1-3-1.5"/></svg>
        <span>41872 Pelton Brook Rd,<br>Farmington MI</span>
      </li>
      <li class="contact__row">
        <svg class="contact__icon" viewBox="0 0 24 24"><circle cx="12" cy="12" r="9"/><path d="M3 12h18M12 3c3 3 3 15 0 18M12 3c-3 3-3 15 0 18M5 7.5h14M5 16.5h14"/></svg>
        <span>www.morvanehairstudio-demo.com</span>
      </li>
      <li class="contact__row">
        <svg class="contact__icon" viewBox="0 0 24 24"><rect x="3" y="3" width="18" height="18" rx="5"/><circle cx="12" cy="12" r="4"/></svg>
        <span>@morvanehairstudio</span>
      </li>
    </ul>
  </div>
</section>

</body>
</html>
```